Business Card *

A business card design
Use the logo uploaded in the brief page.
You may use placeholders in your design layouts.
I will provide the actual business card details to the winning designer.

Logo
Place for contact info (name, title, phone, email, etc)

Requirements
Must have
• Logo

```html
<!DOCTYPE html>
<html lang="en">
<head>
<meta charset="utf-8">
<title>Kestrel Ridge Business Card</title>
<link href="https://fonts.googleapis.com/css2?family=Open+Sans:wght@400;600;700;800&display=swap" rel="stylesheet">
<style>
  :root {
    --backdrop: #2a2a2c;
    --card: #141414;
    --card-edge: #3dbb4a;
    --brand-green: #3dbb4a;
    --lime: #9cc83a;
    --text-light: #e9e9e9;
    --mark-grey: #8e8e8e;
    --emboss: #1c1c1c;
    --rule: #7fae2e;
  }
  * { margin: 0; padding: 0; box-sizing: border-box; }
  html, body { width: 1200px; height: 948px; overflow: hidden; }
  body {
    background: var(--backdrop);
    font-family: "Open Sans", Arial, sans-serif;
    position: relative;
  }
  .card {
    position: absolute;
    width: 560px;
    height: 320px;
    background: var(--card);
    border-radius: 24px;
    border-bottom: 4px solid var(--card-edge);
    overflow: hidden;
  }
  .card--front { left: 70px; top: 130px; }
  .card--back { left: 570px; top: 498px; }

  .brand {
    position: absolute;
    left: 0; right: 0; top: 0; bottom: 0;
    display: flex;
    align-items: center;
    justify-content: center;
    gap: 18px;
  }
  .brand__dot {
    width: 34px; height: 34px;
    border-radius: 50%;
    background: var(--brand-green);
  }
  .brand__name {
    font-weight: 800;
    font-size: 40px;
    letter-spacing: 1px;
    color: var(--mark-grey);
  }

  .back__emboss {
    position: absolute;
    right: -30px; top: -40px;
    width: 280px; height: 280px;
    border-radius: 50%;
    background: var(--emboss);
  }
  .contact {
    position: absolute;
    left: 42px;
    bottom: 34px;
    width: 300px;
    color: var(--text-light);
  }
  .contact__name {
    font-weight: 800;
    font-size: 26px;
    color: var(--brand-green);
    line-height: 1.1;
  }
  .contact__title {
    font-size: 14px;
    color: var(--lime);
    margin-top: 2px;
  }
  .contact__rule {
    height: 1px;
    background: var(--rule);
    margin: 10px 0;
    width: 250px;
  }
  .contact__address { font-size: 14px; line-height: 1.45; }
  .contact__list { list-style: none; font-size: 14px; line-height: 1.7; }
  .contact__list li { display: flex; align-items: center; gap: 10px; }
  .contact__list svg { width: 14px; height: 14px; fill: var(--brand-green); flex: none; }
</style>
</head>
<body>

<section class="card card--front" aria-label="Card front">
  <div class="brand">
    <span class="brand__dot"></span>
    <span class="brand__name">KESTREL RIDGE</span>
  </div>
</section>

<section class="card card--back" aria-label="Card back">
  <div class="back__emboss"></div>
  <div class="contact">
    <h1 class="contact__name">DANA WHITFIELD</h1>
    <p class="contact__title">Owner/CEO</p>
    <div class="contact__rule"></div>
    <p class="contact__address">418 N Alder Road<br>Marlow County 6120</p>
    <div class="contact__rule"></div>
    <ul class="contact__list">
      <li>
        <svg viewBox="0 0 16 16" aria-hidden="true"><path d="M3.5 1l2.5 3-1.5 2a9 9 0 0 0 5 5l2-1.5 3 2.5-1.5 2.5C7 15 1 9 1 2.5z"/></svg>
        555-208-31746
      </li>
      <li>
        <svg viewBox="0 0 16 16" aria-hidden="true"><path d="M1 3h14v10H1z M1.5 3.5L8 9l6.5-5.5" stroke="#141414" stroke-width="1.2"/></svg>
        hello@kestrelridgeag.com
      </li>
      <li>
        <svg viewBox="0 0 16 16" aria-hidden="true"><circle cx="8" cy="8" r="7"/><path d="M1 8h14M8 1c-3 3-3 11 0 14M8 1c3 3 3 11 0 14" stroke="#141414" stroke-width="1" fill="none"/></svg>
        www.kestrelridgeag.com
      </li>
    </ul>
  </div>
</section>

</body>
</html>
```